Text Box for making an update on our website

We need an awesome "Text Box" so that our Users can make an amazing Post or update on our website or App.

Let's make something super duper like Pictavo, Chatterly, Quibb or Posteo text box but a bit more amazing....

I've included our current desktop and Mobile "Text Box" which needs love :)

Our Text Box by default makes a Post "Private" the User can change it to "Public"

I have included what a final "Post" looks like on our site.

Could we incorporate a bit of the "Post" design into the "Create Post" design..... maybe make the header similar.

thanks

Morgan

Target Market(s)

Health Care, Hospitals, Caregivers, Nurses

Industry/Entity Type

Health Care

Font styles to use
Other font styles liked:
• Comfortaa

Requirements
Must have
• Our main colors are

#1D44B8 - Blue
#D85097 - Pink
Nice to have
• Super clean and simple. Happy and Easy to use
Should not have
• Complicated

Too many colors

```html
<!DOCTYPE html>
<html lang="en">
<head>
<meta charset="utf-8">
<title>Create Post</title>
<link href="https://fonts.googleapis.com/css2?family=Arimo:wght@400;700&display=swap" rel="stylesheet">
<style>
  :root {
    --page: #eeeeee;
    --blue: #1d44b8;
    --pink: #d85097;
    --white: #ffffff;
    --placeholder: #b4c2f7;
    --kb-bg: #0b0b0b;
    --key: #555555;
    --key-dark: #2e2e2e;
  }
  * { box-sizing: border-box; margin: 0; padding: 0; }
  html, body { width: 1200px; height: 1200px; overflow: hidden; background: var(--page); }
  body { position: relative; font-family: "Arimo", Arial, sans-serif; }

  .post-composer {
    position: absolute; left: 264px; top: 148px; width: 671px; height: 904px;
    border-radius: 50px 50px 0 0; overflow: hidden; background: var(--blue);
  }
  .header-shape { position: absolute; left: 0; top: 0; }
  .title { position: absolute; left: 47px; top: 18px; color: var(--white); font-size: 27px; font-weight: 400; }
  .close { position: absolute; left: 616px; top: 20px; color: var(--white); font-size: 22px; font-weight: 700; }
  .privacy-pill {
    position: absolute; left: 107px; top: 64px; width: 90px; height: 28px; border-radius: 14px;
    background: var(--white); color: var(--pink); font-size: 15px; line-height: 28px; padding-left: 11px;
  }
  .privacy-pill svg { position: absolute; right: 3px; top: 3px; }

  .editor { position: absolute; left: 0; top: 115px; width: 671px; height: 307px; }
  .editor-bg { position: absolute; left: 0; top: 0; }
  .cursor { position: absolute; left: 46px; top: 174px; width: 2px; height: 30px; background: var(--blue); }
  .placeholder { position: absolute; left: 52px; top: 170px; color: var(--placeholder); font-size: 30px; }
  .emoji-button { position: absolute; left: 506px; top: 337px; }
  .send-button { position: absolute; left: 578px; top: 337px; }

  .toolbar { position: absolute; left: 0; top: 422px; width: 671px; height: 95px; background: var(--blue); }
  .tool { position: absolute; top: 0; width: 160px; margin-left: -80px; text-align: center; color: var(--white); font-size: 18px; }
  .tool svg { display: block; margin: 20px auto 0; height: 40px; }
  .tool span { display: block; margin-top: 4px; }

  .keyboard { position: absolute; left: 0; top: 517px; width: 671px; height: 387px; background: var(--kb-bg); }
  .key {
    position: absolute; height: 74px; border-radius: 8px; background: var(--key);
    color: var(--white); font-size: 36px; display: flex; align-items: center; justify-content: center;
  }
  .key.letter { width: 56px; }
  .key.function { background: var(--key-dark); }
  .key.label { font-size: 26px; }
</style>
</head>
<body>
  <section class="post-composer">
    <svg class="header-shape" width="671" height="160" viewBox="0 0 671 160">
      <path d="M586 0 C570 60 545 100 515 120 L671 120 L671 0 Z" fill="var(--pink)"/>
    </svg>
    <h1 class="title">Create Post</h1>
    <div class="close">x</div>
    <div class="privacy-pill">Private
      <svg width="22" height="22" viewBox="0 0 22 22">
        <circle cx="11" cy="11" r="11" fill="var(--pink)"/>
        <g stroke="#8a3ab0" stroke-width="1.6">
          <line x1="11" y1="3" x2="11" y2="19"/><line x1="3" y1="11" x2="19" y2="11"/>
          <line x1="5.3" y1="5.3" x2="16.7" y2="16.7"/><line x1="16.7" y1="5.3" x2="5.3" y2="16.7"/>
        </g>
      </svg>
    </div>

    <div class="editor">
      <svg class="editor-bg" width="671" height="307" viewBox="0 0 671 307">
        <rect x="0" y="0" width="671" height="307" fill="var(--pink)"/>
        <rect x="0" y="0" width="520" height="307" fill="var(--blue)"/>
        <path d="M0 37 Q10 0 80 0 L591 0 Q661 0 671 37 L671 307 L0 307 Z" fill="var(--white)"/>
      </svg>
      <div class="cursor"></div>
      <div class="placeholder">Share a new post</div>
      <svg class="emoji-button" width="58" height="58" viewBox="0 0 58 58">
        <circle cx="29" cy="29" r="27" fill="none" stroke="var(--pink)" stroke-width="2.5"/>
        <circle cx="19" cy="23" r="3" fill="var(--pink)"/>
        <circle cx="39" cy="23" r="3" fill="var(--pink)"/>
        <path d="M17 36 Q29 45 41 36" fill="none" stroke="var(--pink)" stroke-width="2.5" stroke-linecap="round"/>
      </svg>
      <svg class="send-button" width="58" height="58" viewBox="0 0 58 58">
        <circle cx="29" cy="29" r="28" fill="var(--blue)"/>
        <path d="M15 17 L45 29 L15 41 L19 29 Z" fill="var(--white)"/>
        <line x1="19" y1="29" x2="36" y2="29" stroke="var(--blue)" stroke-width="2"/>
      </svg>
    </div>

    <nav class="toolbar">
      <div class="tool" style="left:108px">
        <svg width="50" height="40" viewBox="0 0 50 40">
          <rect x="8" y="2" width="40" height="30" rx="2" fill="none" stroke="var(--white)" stroke-width="2.5"/>
          <rect x="2" y="9" width="40" height="30" rx="3" fill="var(--white)"/>
        </svg><span>Add photos</span>
      </div>
      <div class="tool" style="left:265px">
        <svg width="26" height="40" viewBox="0 0 26 40">
          <path d="M13 39 C5 27 1 20 1 13 A12 12 0 0 1 25 13 C25 20 21 27 13 39 Z" fill="var(--white)"/>
          <circle cx="13" cy="12" r="4.5" fill="var(--blue)"/>
        </svg><span>Check-In</span>
      </div>
      <div class="tool" style="left:423px">
        <svg width="40" height="40" viewBox="0 0 40 40">
          <circle cx="20" cy="20" r="18.5" fill="none" stroke="var(--white)" stroke-width="2"/>
          <circle cx="20" cy="15" r="7" fill="var(--white)"/>
          <path d="M8 33 Q10 23 20 23 Q30 23 32 33 Q26 38 20 38 Q14 38 8 33 Z" fill="var(--white)"/>
        </svg><span>Tag Friends</span>
      </div>
      <div class="tool" style="left:576px">
        <svg width="40" height="40" viewBox="0 0 40 40">
          <path d="M14 34 L31 12 A5 5 0 0 0 23 6 L7 27 A3 3 0 0 0 12 31 L25 14" fill="none" stroke="var(--white)" stroke-width="2.2" stroke-linecap="round"/>
        </svg><span>Add files</span>
      </div>
    </nav>

    <div class="keyboard">
      <div class="key letter" style="left:5px;top:15px">q</div>
      <div class="key letter" style="left:72px;top:15px">w</div>
      <div class="key letter" style="left:139px;top:15px">e</div>
      <div class="key letter" style="left:206px;top:15px">r</div>
      <div class="key letter" style="left:273px;top:15px">t</div>
      <div class="key letter" style="left:341px;top:15px">y</div>
      <div class="key letter" style="left:408px;top:15px">u</div>
      <div class="key letter" style="left:475px;top:15px">i</div>
      <div class="key letter" style="left:542px;top:15px">o</div>
      <div class="key letter" style="left:609px;top:15px">p</div>

      <div class="key letter" style="left:38px;top:111px">a</div>
      <div class="key letter" style="left:105px;top:111px">s</div>
      <div class="key letter" style="left:172px;top:111px">d</div>
      <div class="key letter" style="left:239px;top:111px">f</div>
      <div class="key letter" style="left:307px;top:111px">g</div>
      <div class="key letter" style="left:374px;top:111px">h</div>
      <div class="key letter" style="left:441px;top:111px">j</div>
      <div class="key letter" style="left:508px;top:111px">k</div>
      <div class="key letter" style="left:575px;top:111px">l</div>

      <div class="key function" style="left:5px;top:208px;width:75px">
        <svg width="38" height="32" viewBox="0 0 38 32"><path d="M19 3 L35 18 L27 18 L27 29 L11 29 L11 18 L3 18 Z" fill="none" stroke="var(--white)" stroke-width="2" stroke-linejoin="round"/></svg>
      </div>
      <div class="key letter" style="left:105px;top:208px">z</div>
      <div class="key letter" style="left:172px;top:208px">x</div>
      <div class="key letter" style="left:239px;top:208px">c</div>
      <div class="key letter" style="left:307px;top:208px">v</div>
      <div class="key letter" style="left:374px;top:208px">b</div>
      <div class="key letter" style="left:441px;top:208px">n</div>
      <div class="key letter" style="left:508px;top:208px">m</div>
      <div class="key function" style="left:590px;top:208px;width:75px">
        <svg width="42" height="30" viewBox="0 0 42 30"><path d="M12 2 L39 2 L39 28 L12 28 L2 15 Z" fill="none" stroke="var(--white)" stroke-width="2" stroke-linejoin="round"/><path d="M19 9 L31 21 M31 9 L19 21" stroke="var(--white)" stroke-width="2"/></svg>
      </div>

      <div class="key function label" style="left:5px;top:301px;width:72px">123</div>
      <div class="key function" style="left:89px;top:301px;width:72px">
        <svg width="38" height="38" viewBox="0 0 38 38"><circle cx="19" cy="19" r="16.5" fill="none" stroke="var(--white)" stroke-width="2.5"/><circle cx="13" cy="14" r="2.5" fill="var(--white)"/><circle cx="25" cy="14" r="2.5" fill="var(--white)"/><path d="M9 20 L29 20 Q27 30 19 30 Q11 30 9 20 Z" fill="var(--white)"/></svg>
      </div>
      <div class="key function" style="left:173px;top:301px;width:56px">
        <svg width="24" height="38" viewBox="0 0 24 38"><rect x="7" y="2" width="10" height="21" rx="5" fill="none" stroke="var(--white)" stroke-width="2"/><path d="M3 17 Q3 29 12 29 Q21 29 21 17 M12 29 L12 36 M6 36 L18 36" fill="none" stroke="var(--white)" stroke-width="2"/></svg>
      </div>
      <div class="key label" style="left:239px;top:301px;width:258px">space</div>
      <div class="key function label" style="left:509px;top:301px;width:156px">return</div>
    </div>
  </section>
</body>
</html>
```